Corvale Mechanical - Letterhead

We are a plumbing and hvac company based in Calgary. This letterhead will be on our quotes, invoices, preventative maintenance proposals etc.

```html
<!DOCTYPE html>
<html lang="en">
<head>
<meta charset="utf-8">
<title>Corvale Mechanical – Letterhead</title>
<link href="https://fonts.googleapis.com/css2?family=Open+Sans:wght@400;600;700;800&display=swap" rel="stylesheet">
<style>
  :root{
    --brand-orange:#ee6336;
    --brand-blue:#3a78c0;
    --ink:#333333;
    --paper:#ffffff;
    --backdrop:#d9d9d9;
  }
  *{margin:0;padding:0;box-sizing:border-box;}
  html,body{width:1056px;height:1200px;overflow:hidden;background:var(--backdrop);}
  body{font-family:"Open Sans",sans-serif;color:var(--ink);}
  .letterhead{
    position:absolute;left:125px;top:30px;width:806px;height:1140px;
    background:var(--paper);overflow:hidden;
    box-shadow:0 10px 30px rgba(0,0,0,.18);
  }
  .brand{
    position:absolute;left:81px;top:42px;width:225px;
    text-align:center;color:var(--brand-blue);font-weight:800;
  }
  .brand-dot{
    width:62px;height:62px;border-radius:50%;
    background:var(--brand-orange);margin:0 auto 12px;
  }
  .brand-name{font-size:38px;line-height:1;letter-spacing:1px;}
  .brand-sub{font-size:13px;letter-spacing:2px;margin-top:6px;}
  .letter-date,.recipient,.salutation,.letter-body,.closing{position:absolute;left:82px;}
  .letter-date{top:444px;font-size:12px;}
  .letter-date{top:253px;}
  .recipient{top:290px;font-size:12px;line-height:22px;}
  .salutation{top:402px;font-size:18px;font-weight:600;}
  .letter-body{top:458px;width:640px;font-size:11.8px;line-height:22.5px;}
  .letter-body p{text-align:justify;margin-bottom:21px;}
  .closing{top:856px;font-size:12px;}
  .signature{
    position:absolute;left:82px;top:906px;width:100px;height:36px;
    background:linear-gradient(90deg,rgba(58,120,192,.35),rgba(58,120,192,.1));
    border-radius:18px;
  }
  .footer-band{position:absolute;left:0;bottom:0;width:100%;height:57px;display:flex;}
  .footer-band .left{flex:0 0 403px;background:var(--brand-orange);}
  .footer-band .right{flex:1;background:var(--brand-blue);}
  .footer-badge{
    position:absolute;left:353px;top:1035px;width:100px;height:100px;border-radius:50%;
    background:var(--paper);
  }
  .footer-badge::after{
    content:"";position:absolute;inset:10px;border-radius:50%;background:var(--brand-orange);
  }
  .contact{position:absolute;color:#fff;font-size:12px;font-weight:700;line-height:20px;}
  .contact.left{left:60px;top:1090px;}
  .contact.right{left:506px;top:1090px;}
  .contact li{list-style:none;display:flex;align-items:center;gap:8px;}
  .contact svg{width:11px;height:11px;flex:0 0 11px;}
</style>
</head>
<body>
<main class="letterhead">
  <header class="brand">
    <div class="brand-dot"></div>
    <div class="brand-name">CORVALE</div>
    <div class="brand-sub">MECHANICAL INC</div>
  </header>

  <p class="letter-date">September 10th, 2020</p>
  <address class="recipient" style="font-style:normal">
    First Last Name<br>Street Address<br>City, State 00000
  </address>

  <h1 class="salutation">Dear Sir / Mam,</h1>

  <section class="letter-body">
    <p>Lorem ipsum dolor sit amet, consectetur adipiscing elit. Aenean ut ipsum eget massa hendrerit vestibulum vel in velit. Donec pretium neque velit.</p>
    <p>Aliquam porta lectus nec mauris ornare venenatis. Vivamus non est turpis, et cursus sem. Mauris vehicula erat in diam auctor at bibendum nisl lacinia.</p>
    <p>Morbi imperdiet neque vehicula nunc convallis gravida. Vestibulum iaculis pretium placerat. Integer consequat, est sit amet facilisis eleifend, nibh nibh varius orci, eget dapibus arcu dui non purus. Pellentesque in magna mauris. Duis enim sapien, dictum vitae condimentum a, pulvinar vel lacus. Mauris et molestie nibh. Vestibulum vitae nulla at metus elementum porta sit amet interdum elit. Nulla sollicitudin neque eu nulla volutpat congue.</p>
    <p>Etiam pellentesque, velit id dapibus fermentum, turpis sapien ornare dui, ac tincidunt ligula odio congue purus. Nunc sed ante dui, in porta lectus. Cras nec sem lorem. In hac habitasse platea dictumst. Maecenas id diam quis dui porta tristique. Sed id egestas felis. Donec ullamcorper mattis posuere. Phasellus fermentum eleifend tortor vel dapibus. Vestibulum ante ipsum.</p>
  </section>

  <p class="closing">Your Sincerely,</p>
  <div class="signature" role="img" aria-label="Handwritten signature"></div>

  <footer>
    <div class="footer-band"><div class="left"></div><div class="right"></div></div>
    <div class="footer-badge"></div>
    <ul class="contact left">
      <li><svg viewBox="0 0 12 12"><circle cx="6" cy="6" r="6" fill="#3a78c0"/><path d="M6 3a2 2 0 0 0-2 2c0 1.5 2 4 2 4s2-2.5 2-4a2 2 0 0 0-2-2z" fill="#fff"/></svg>410 Beltline Avenue #600 Calgary, AB T2R 0B4</li>
      <li><svg viewBox="0 0 12 12"><circle cx="6" cy="6" r="6" fill="#3a78c0"/><path d="M4 3l1.3 1.6-.7.9c.4.8 1 1.4 1.9 1.9l.9-.7L9 8l-.8 1C6 9 3 6 3 3.8z" fill="#fff"/></svg>403-555-0182</li>
    </ul>
    <ul class="contact right">
      <li><svg viewBox="0 0 12 12"><circle cx="6" cy="6" r="6" fill="#ee6336"/><rect x="3" y="4" width="6" height="4" fill="#fff"/></svg>info@corvalemechanical.com</li>
      <li><svg viewBox="0 0 12 12"><circle cx="6" cy="6" r="6" fill="#ee6336"/><circle cx="6" cy="6" r="2.6" fill="none" stroke="#fff" stroke-width="1"/></svg>www.corvalemechanical.com</li>
    </ul>
  </footer>
</main>
</body>
</html>
```